Wordpress website re-design

Update existing 5 page wordpress website to look more professional. We run a 10 week boxing program that ends in a black tie gala event.

We would like to keep the existing pink hero colour.

The website:
- must be Wordpress
- prefer it to work with the Elementor plugin for easy future changes
- Keep the existing URL structure
- Use white space/backgrounds - D not want all black background or the pink colour used as the background for an entire section
- Shouldn't look too 'templatey'. Good flow between sections

Logo, images and video to use can be found here: https://share.quorvexfiles.net/folders/8hTqzW2mLpRvBn4kXcYd_JsEaGfUoNiM-?view=public

Website to be redesigned: https://bellmoreshowcase.com.au/

Designs look the same

Target Market(s)

Men working office jobs aged 28-38

Coding

Coded - Design and coding required

Number of Pages Required

5+ page

Colors

Designer to choose colors to be used in the design.

Requirements
Must have
• Wordpress
Nice to have
• Work with Elementor so that I can easily make changes in the future
Should not have
• Entirely black background. Want it to be lighter / plenty of white background. Not too blocky - flowing through sections and some of the images with backgrounds removed to make it less blocky also. I do not want it to be clerly 'templatey'. The pink should be used as a hero colour, not for entire sections

```html
<!DOCTYPE html>
<html lang="en">
<head>
<meta charset="utf-8">
<title>Ring For Purpose</title>
<link href="https://fonts.googleapis.com/css2?family=Roboto+Condensed:wght@400;700&family=Roboto:wght@400;500;700&display=swap" rel="stylesheet">
<style>
:root{
  --pink:#f0105f;
  --ink:#222;
  --muted:#6b6b6b;
  --line:#e6e6e6;
  --soft:#f6f6f6;
  --white:#fff;
  --gold:#d89a2a;
}
*{box-sizing:border-box;margin:0;padding:0}
html,body{width:1200px;height:4369px;overflow:hidden;background:var(--white)}
body{font-family:'Roboto',sans-serif;color:var(--ink);position:relative}
.abs{position:absolute}
h1,h2,h3,.cond{font-family:'Roboto Condensed',sans-serif}
.btn{position:absolute;display:flex;align-items:center;justify-content:center;gap:8px;background:var(--pink);color:#fff;font-family:'Roboto Condensed',sans-serif;font-weight:700;font-size:12px;text-transform:uppercase;border-radius:3px;letter-spacing:.2px}
.btn svg{width:13px;height:13px}
.brand{font-family:'Roboto Condensed',sans-serif;font-weight:700;color:var(--pink);text-transform:uppercase;line-height:1}

/* header */
.site-header{left:0;top:0;width:1200px;height:105px;background:#fff}
.site-header .brand{position:absolute;left:81px;top:32px;font-size:20px;line-height:21px;width:110px}
.site-header .brand .mark{display:inline-block;width:9px;height:9px;background:var(--pink);border-radius:50%;margin-left:6px}
.nav{position:absolute;left:373px;top:44px;display:flex;gap:26px;font-family:'Roboto Condensed',sans-serif;font-size:12.5px;text-transform:uppercase;color:var(--ink)}
.nav .active{color:var(--pink)}
.site-header .btn{left:1000px;top:34px;width:109px;height:38px}

/* hero */
.hero{left:0;top:105px;width:1200px;height:570px;background:
  linear-gradient(90deg,rgba(8,6,8,.92) 0%,rgba(8,6,8,.7) 38%,rgba(8,6,8,0) 60%),
  radial-gradient(ellipse 120px 230px at 935px 300px,rgba(220,40,55,.85),rgba(220,40,55,0)),
  radial-gradient(ellipse 90px 120px at 940px 110px,rgba(210,30,45,.9),rgba(210,30,45,0)),
  radial-gradient(ellipse 110px 200px at 720px 290px,rgba(60,90,190,.75),rgba(60,90,190,0)),
  radial-gradient(ellipse 160px 260px at 1170px 220px,rgba(40,70,150,.7),rgba(40,70,150,0)),
  linear-gradient(180deg,#141218 0%,#2a2430 45%,#3b3338 70%,#0a090b 100%)}
.hero h1{position:absolute;left:81px;top:150px;font-size:41px;line-height:44px;color:var(--pink);text-transform:uppercase;font-weight:700}
.hero p{position:absolute;left:81px;width:405px;color:#fff;font-size:14px;line-height:19px}
.hero .btn{left:81px;top:383px;width:220px;height:38px}

/* video */
.video{position:absolute;background:
  radial-gradient(ellipse 160px 90px at 420px 110px,rgba(230,235,255,.75),rgba(230,235,255,0)),
  radial-gradient(ellipse 200px 70px at 260px 240px,rgba(160,170,240,.5),rgba(160,170,240,0)),
  linear-gradient(180deg,#1d2a6b 0%,#3145b0 45%,#1a2470 75%,#0c1038 100%);overflow:hidden}
.video .bar{position:absolute;left:10px;top:14px;color:#fff;font-size:14px;display:flex;align-items:center;gap:10px}
.video .bar .dot{width:30px;height:30px;border-radius:50%;background:#fff}
.video .tools{position:absolute;right:25px;top:34px;color:#fff;font-size:12px;display:flex;gap:22px}
.video .play{position:absolute;left:50%;top:50%;width:60px;height:42px;margin:-21px 0 0 -30px;border-radius:10px;background:var(--pink);display:flex;align-items:center;justify-content:center}
.video .watch{position:absolute;left:0;bottom:0;padding:10px 16px;background:rgba(0,0,0,.75);color:#fff;font-size:13px;font-weight:500;border-top-right-radius:8px}

.title{font-family:'Roboto Condensed',sans-serif;font-weight:700;font-size:30px;color:var(--ink);line-height:34px}
.body-sm{font-size:12.5px;line-height:20.5px;color:var(--muted)}
.ticks{list-style:none}
.ticks li{display:flex;align-items:center;gap:12px;font-size:12.5px;color:#444;height:33px;border-bottom:1px solid var(--line)}
.ticks svg{width:11px;height:11px;flex:none}

/* photo panels */
.photo-circle{background:
  radial-gradient(ellipse 70px 120px at 255px 230px,rgba(235,40,45,1),rgba(235,40,45,0)),
  radial-gradient(ellipse 90px 60px at 250px 360px,rgba(240,60,60,.9),rgba(240,60,60,0)),
  radial-gradient(ellipse 80px 70px at 240px 110px,rgba(230,185,160,.8),rgba(230,185,160,0)),
  radial-gradient(ellipse 90px 150px at 110px 230px,rgba(20,20,24,.95),rgba(20,20,24,0)),
  linear-gradient(160deg,#7a6e6c 0%,#4a4448 45%,#2a2628 100%)}
.photo-cost{background:
  radial-gradient(ellipse 110px 90px at 200px 280px,rgba(60,100,220,.9),rgba(60,100,220,0)),
  radial-gradient(ellipse 100px 90px at 340px 280px,rgba(220,40,50,.85),rgba(220,40,50,0)),
  radial-gradient(ellipse 60px 90px at 140px 320px,rgba(230,230,235,.7),rgba(230,230,235,0)),
  radial-gradient(ellipse 200px 60px at 260px 450px,rgba(180,185,210,.5),rgba(180,185,210,0)),
  radial-gradient(ellipse 260px 140px at 260px 60px,rgba(90,90,200,.7),rgba(90,90,200,0)),
  linear-gradient(180deg,#23266a 0%,#15183f 50%,#07081a 100%)}

/* features */
.card{position:absolute;width:512px;background:#fff;border:1px solid #ececec;border-radius:8px;box-shadow:0 2px 8px rgba(0,0,0,.07);padding:24px 24px 0 82px}
.card .ico{position:absolute;left:24px;top:22px;width:40px;height:40px}
.card h3{font-size:16px;font-weight:700;color:var(--ink);margin-top:14px;margin-bottom:6px}
.card p{font-size:11.5px;line-height:18px;color:#8a8a8a}

/* pricing */
.price-box{position:absolute;left:636px;top:3792px;width:456px;height:81px;background:var(--pink);border-radius:4px;color:#fff;padding:18px 26px}
.price-box strong{display:block;font-size:24px;font-weight:700}
.price-box span{font-size:12px}
</style>
</head>
<body>

<header class="abs site-header">
  <div class="brand">Ring For Purpose<span class="mark"></span></div>
  <nav class="nav">
    <span class="active">Home</span><span>About The Program</span><span>Meet The Team</span><span>Past Fighters</span><span>Contact Us</span>
  </nav>
  <a class="btn">Join Now</a>
</header>

<section class="abs hero" role="img" aria-label="Photo of two amateur boxers in red and blue gear fighting in a ring under arena lights">
  <h1>From Desk To The<br>Ring In 10 Weeks!</h1>
  <p style="top:250px">We help people like you go from little or no boxing experience to a boxing bout in 10 weeks. Get fit, have fun and support charity in a safe environment.</p>
  <p style="top:325px">Want to be the first to know when the next program starts?</p>
  <a class="btn">Notify Me Of Next Program</a>
</section>

<section class="about">
  <h2 class="abs" style="left:81px;top:842px;font-size:31px;font-weight:700;color:var(--pink)">WHAT'S IT ALL ABOUT?</h2>
  <p class="abs" style="left:81px;top:893px;width:370px;font-size:19px;line-height:28px;color:#333">RFP has helped raise over $460,000 for charity so far. Let's keep making a difference!</p>
  <div class="video" style="left:503px;top:737px;width:616px;height:344px" role="img" aria-label="Highlight reel video of the gala fight night arena">
    <div class="bar"><span class="dot"></span>RFP || Highlight Reel</div>
    <div class="tools"><span>Watch Later</span><span>Share</span></div>
    <div class="play"><svg width="18" height="20" viewBox="0 0 22 24"><path d="M2 1l19 11L2 23z" fill="#fff"/></svg></div>
    <div class="watch">Watch on VidStream</div>
  </div>
</section>

<section class="what">
  <svg class="abs" style="left:127px;top:1203px" width="415" height="407" viewBox="0 0 415 407" role="img" aria-label="Boxer in red walking to the ring, cut into an angular shape">
    <defs>
      <radialGradient id="gRed" cx=".5" cy=".55" r=".25"><stop offset="0" stop-color="#e02a30"/><stop offset="1" stop-color="#e02a30" stop-opacity="0"/></radialGradient>
      <radialGradient id="gWarm" cx=".75" cy=".4" r=".35"><stop offset="0" stop-color="#a08a78"/><stop offset="1" stop-color="#a08a78" stop-opacity="0"/></radialGradient>
      <linearGradient id="gBase" x1="0" y1="0" x2="1" y2="1"><stop offset="0" stop-color="#3a3330"/><stop offset=".55" stop-color="#1f1b1a"/><stop offset="1" stop-color="#4a3e38"/></linearGradient>
    </defs>
    <polygon id="cut" points="215,0 330,120 300,132 415,205 300,318 258,407 130,330 0,245 82,160 150,80" fill="url(#gBase)"/>
    <polygon points="215,0 330,120 300,132 415,205 300,318 258,407 130,330 0,245 82,160 150,80" fill="url(#gWarm)"/>
    <polygon points="215,0 330,120 300,132 415,205 300,318 258,407 130,330 0,245 82,160 150,80" fill="url(#gRed)"/>
  </svg>
  <h2 class="abs title" style="left:614px;top:1280px">What Is Ring For Purpose?</h2>
  <p class="abs body-sm" style="left:614px;top:1329px;width:500px">Ring For Purpose is a 10 Week Program, raising much needed funds for charity, whilst providing everyday people the experience of stepping into a boxing ring in front of a packed arena with friends, family and colleagues cheering you on!</p>
  <p class="abs body-sm" style="left:614px;top:1411px;width:500px">The program is designed for people with little or no boxing experience. Our world class trainers will guide you through the process from complete beginner to being prepared for your first amateur boxing fight.</p>
  <a class="btn" style="left:614px;top:1492px;width:135px;height:39px">Learn More <svg viewBox="0 0 14 14"><circle cx="7" cy="7" r="6" fill="none" stroke="#fff" stroke-width="1.5"/><path d="M5 4.5L8 7 5 9.5" fill="none" stroke="#fff" stroke-width="1.5"/></svg></a>
</section>

<section class="abs" style="left:0;top:1670px;width:1200px;height:466px;background:var(--soft)">
  <h2 class="abs title" style="left:81px;top:200px">Take A Look At Your Next<br>Experience</h2>
  <div class="abs" style="left:503px;top:61px;width:616px;height:344px;background:#000;display:flex;align-items:center;justify-content:center">
    <div class="brand" style="font-size:54px;text-align:center;line-height:58px">Ring For<br>Purpose</div>
  </div>
</section>

<section class="why">
  <div class="abs photo-circle" style="left:132px;top:2198px;width:405px;height:405px;border-radius:50%" role="img" aria-label="Victorious boxer in red raising his arms beside the referee"></div>
  <h2 class="abs title" style="left:614px;top:2255px">Why Ring For Purpose?</h2>
  <p class="abs" style="left:614px;top:2310px;width:500px;font-size:12.5px;line-height:20.5px;font-weight:500;color:#333">If getting fit, supporting charity and having a good time in a safe environment sound appealing, then Ring For Purpose is the program for you.</p>
  <ul class="abs ticks" style="left:614px;top:2359px;width:505px">
    <li><svg viewBox="0 0 12 12"><path d="M1 6l3.5 3.5L11 2" fill="none" stroke="#f0105f" stroke-width="2"/></svg>Lose weight and get fit</li>
    <li><svg viewBox="0 0 12 12"><path d="M1 6l3.5 3.5L11 2" fill="none" stroke="#f0105f" stroke-width="2"/></svg>Fight in front of friends, family and coworkers at the exclusive black tie dinner</li>
    <li><svg viewBox="0 0 12 12"><path d="M1 6l3.5 3.5L11 2" fill="none" stroke="#f0105f" stroke-width="2"/></svg>Learn valuable boxing skills</li>
    <li><svg viewBox="0 0 12 12"><path d="M1 6l3.5 3.5L11 2" fill="none" stroke="#f0105f" stroke-width="2"/></svg>Build friendships with your fellow fighters</li>
  </ul>
  <a class="btn" style="left:614px;top:2502px;width:135px;height:39px">Learn More <svg viewBox="0 0 14 14"><circle cx="7" cy="7" r="6" fill="none" stroke="#fff" stroke-width="1.5"/><path d="M5 4.5L8 7 5 9.5" fill="none" stroke="#fff" stroke-width="1.5"/></svg></a>
</section>

<section class="abs" style="left:0;top:2661px;width:1200px;height:446px;background:var(--soft)">
  <h2 class="abs title" style="left:81px;top:78px">What Charity Is Being Supported?</h2>
  <div class="abs" style="left:810px;top:70px;display:flex;align-items:center;gap:10px;font-family:'Roboto',sans-serif;font-weight:700;font-size:20px;color:var(--gold);line-height:22px"><span style="width:40px;height:40px;border-radius:50%;background:var(--gold)"></span>Halvane<br>Foundation</div>
  <p class="abs body-sm" style="left:81px;top:150px;width:1040px">Ring For Purpose is pleased to be supporting Halvane Foundation.</p>
  <p class="abs body-sm" style="left:81px;top:184px;width:1040px">Halvane Foundation is a non-profit humanitarian organisation set on valuing all lives equally through acts of service. Halvane operates globally, delivering care to some of the most vulnerable.</p>
  <p class="abs body-sm" style="left:81px;top:240px;width:1040px">Their mission mission can be easily remembered with an acronym; "HELP" which stands for: Healthcare, Education, Living essentials (water, food, shelter), Providing opportunities and life skills.</p>
  <p class="abs body-sm" style="left:81px;top:294px;width:1040px">The event will raise essential funds for administering basic healthcare for children of vulnerable and underprivileged backgrounds.</p>
  <a class="btn" style="left:81px;top:346px;width:135px;height:39px">Learn More <svg viewBox="0 0 14 14"><circle cx="7" cy="7" r="6" fill="none" stroke="#fff" stroke-width="1.5"/><path d="M5 4.5L8 7 5 9.5" fill="none" stroke="#fff" stroke-width="1.5"/></svg></a>
</section>

<section class="features">
  <div class="card" style="left:81px;top:3161px;height:153px">
    <svg class="ico" viewBox="0 0 40 40"><rect x="3" y="7" width="30" height="28" rx="3" fill="none" stroke="#f0105f" stroke-width="2.5"/><path d="M3 14h30M11 3v8M25 3v8" stroke="#f0105f" stroke-width="2.5"/><text x="11" y="30" font-size="12" font-family="Roboto" font-weight="700" fill="#f0105f">10</text></svg>
    <h3 class="cond">3 Weekly Training Sessions For 10 Weeks</h3>
    <p>Training takes place each Tuesday, Thursday and Saturday throughout the 10 week program.</p>
  </div>
  <div class="card" style="left:605px;top:3161px;height:153px">
    <svg class="ico" viewBox="0 0 40 40"><path d="M20 4l14 8v16l-14 8-14-8V12z" fill="none" stroke="#f0105f" stroke-width="5"/></svg>
    <h3 class="cond">Fight Kit</h3>
    <p>We provide a full fight kit so that you're ready to train from day 1. This includes boxing gloves, wraps and head gear.<br>All you need to provide is a personal mouth guard and groin protection suited to your individual needs.</p>
  </div>
  <div class="card" style="left:81px;top:3327px;height:139px">
    <svg class="ico" viewBox="0 0 40 40"><text x="10" y="34" font-size="40" font-family="Roboto" font-weight="700" fill="#f0105f">$</text></svg>
    <h3 class="cond">Membership To Steadfast Boxing</h3>
    <p>All Ring For Purpose fighters receive full membership to Steadfast Boxing for the duration of the program. This means you can attend additional classes as you desire at no extra cost.</p>
  </div>
  <div class="card" style="left:605px;top:3327px;height:139px">
    <svg class="ico" viewBox="0 0 40 40"><rect x="6" y="4" width="28" height="32" fill="#f0105f"/><path d="M14 10l6 10 6-10z" fill="#fff"/></svg>
    <h3 class="cond">Black Tie Fight Night</h3>
    <p>Experience the glory of fighting in front of your friends, family and co-workers while they sit down to a two course black tie dinner.</p>
  </div>
  <div class="card" style="left:81px;top:3480px;height:156px">
    <svg class="ico" viewBox="0 0 40 40" fill="#f0105f"><circle cx="20" cy="12" r="7"/><circle cx="8" cy="15" r="5"/><circle cx="32" cy="15" r="5"/><path d="M8 34c0-9 5-14 12-14s12 5 12 14z"/><path d="M0 32c0-6 3-10 8-10 2 0 3 1 4 2-3 3-4 6-4 8zM40 32c0-6-3-10-8-10-2 0-3 1-4 2 3 3 4 6 4 8z"/></svg>
    <h3 class="cond">World Class Trainers</h3>
    <p>Be trained by the best of the best, including active professional boxers.</p>
  </div>
  <div class="card" style="left:605px;top:3480px;height:156px">
    <svg class="ico" viewBox="0 0 40 40" fill="#f0105f"><path d="M6 18c0-6 4-10 10-10h8c4 0 6 3 6 6v4l4 2v8c0 5-4 8-9 8H16C10 36 6 32 6 26z"/></svg>
    <h3 class="cond">Fair Matchmaking</h3>
    <p>Our experienced trainers will ensure you are matched with someone of a comparable skill level and size.<br>Our goal is to ensure all fighters have a good time, go the full 3 rounds and most importantly, don't get hurt.</p>
  </div>
</section>

<section class="pricing">
  <div class="abs photo-cost" style="left:73px;top:3687px;width:527px;height:615px;border-radius:10px" role="img" aria-label="Two boxers exchanging punches in the ring while the referee watches"></div>
  <h2 class="abs title" style="left:636px;top:3742px">What's The Cost?</h2>
  <div class="price-box cond"><strong>Full 10 week program</strong><span style="font-family:'Roboto',sans-serif">Pay up front</span></div>
  <p class="abs" style="left:636px;top:3900px;font-size:24px;font-weight:700;color:#333">$895</p>
  <p class="abs" style="left:636px;top:3932px;font-size:13px;color:var(--muted)">Once off</p>
  <ul class="abs ticks" style="left:636px;top:3960px;width:456px">
    <li><svg viewBox="0 0 12 12"><path d="M1 6l3.5 3.5L11 2" fill="none" stroke="#f0105f" stroke-width="2"/></svg>10 weeks of training</li>
    <li><svg viewBox="0 0 12 12"><path d="M1 6l3.5 3.5L11 2" fill="none" stroke="#f0105f" stroke-width="2"/></svg>Fight kit</li>
    <li><svg viewBox="0 0 12 12"><path d="M1 6l3.5 3.5L11 2" fill="none" stroke="#f0105f" stroke-width="2"/></svg>Official amateur fight</li>
    <li><svg viewBox="0 0 12 12"><path d="M1 6l3.5 3.5L11 2" fill="none" stroke="#f0105f" stroke-width="2"/></svg>Insurance</li>
    <li style="border-bottom:0"><svg viewBox="0 0 12 12"><path d="M1 6l3.5 3.5L11 2" fill="none" stroke="#f0105f" stroke-width="2"/></svg>Membership to Steadfast Boxing</li>
  </ul>
  <a class="btn" style="left:636px;top:4144px;width:119px;height:39px">Join Now <svg viewBox="0 0 14 14"><circle cx="7" cy="7" r="6" fill="none" stroke="#fff" stroke-width="1.5"/><path d="M5 4.5L8 7 5 9.5" fill="none" stroke="#fff" stroke-width="1.5"/></svg></a>
  <p class="abs" style="left:636px;top:4204px;width:460px;font-size:10px;line-height:14px;color:#8a8a8a"><b>Note:</b> Each fighter is responsible for selling 2 x tables (20 tickets) for the Black Tie Dinner Event.</p>
</section>

</body>
</html>
```